Halden Roamer 340 mid roof wrap for remodeling company

I think most car wraps are tacky. I want to keep it simple and clean. No full wraps, it should be a partial wrap, and I want the main color to be white.

Black and white is best, but if adding one or two more colors would work best, we can do that. Gray would be the first choice, and maybe one more like red or blue if needed.

I included a photo of the blank van photos with my logos superimposed in the way I have them on my current vehicle. I do want to keep the same fonts, info, and arrow logo.

```html
<!DOCTYPE html>
<html lang="en">
<head>
<meta charset="utf-8">
<title>Broadview Homes – Halden Roamer 340 Side Wrap</title>
<link rel="stylesheet" href="https://fonts.googleapis.com/css2?family=Montserrat:wght@400;600;700;800&display=swap">
<style>
  :root {
    --stage: #e9ebee;
    --panel: #ffffff;
    --ink: #161616;
    --gray-dark: #8c8c8c;
    --gray-mid: #b9b9b9;
    --gray-light: #dcdcdc;
  }
  html, body {
    margin: 0;
    padding: 0;
    width: 1200px;
    height: 900px;
    overflow: hidden;
    background: var(--stage);
  }
  .canvas {
    position: relative;
    width: 1200px;
    height: 900px;
    font-family: "Montserrat", sans-serif;
    color: var(--ink);
  }
  .wrap-panel {
    position: absolute;
    left: 74px;
    top: 175px;
    width: 1060px;
    height: 390px;
    background: var(--panel);
    border-radius: 34px 60px 18px 18px;
    box-shadow: 0 2px 10px rgba(0,0,0,0.08);
    overflow: hidden;
  }
  .wrap-graphics {
    position: absolute;
    inset: 0;
  }
  .brand-name {
    position: absolute;
    left: 288px;
    top: 78px;
    margin: 0;
    font-weight: 600;
    color: var(--ink);
    line-height: 1;
  }
  .brand-name .line-one {
    display: block;
    font-size: 42px;
    letter-spacing: 0.2em;
  }
  .brand-name .line-two {
    display: block;
    font-size: 30px;
    letter-spacing: 0.22em;
    margin-top: 14px;
  }
  .tagline {
    position: absolute;
    left: 290px;
    top: 183px;
    margin: 0;
    font-size: 19px;
    font-weight: 800;
    letter-spacing: 0.1em;
  }
  .contact {
    position: absolute;
    left: 400px;
    top: 248px;
    margin: 0;
    font-weight: 700;
    line-height: 1.3;
  }
  .contact .phone {
    display: block;
    font-size: 16px;
    letter-spacing: 0.12em;
  }
  .contact .web,
  .contact .town {
    display: block;
    font-size: 12.5px;
    letter-spacing: 0.06em;
  }
  .license {
    position: absolute;
    left: 778px;
    top: 250px;
    margin: 0;
    font-size: 10px;
    font-weight: 700;
  }
</style>
</head>
<body>
<main class="canvas">
  <section class="wrap-panel" aria-label="Van side wrap layout">
    <svg class="wrap-graphics" width="1060" height="390" viewBox="0 0 1060 390" aria-hidden="false">
      <defs>
        <linearGradient id="halftone-fade" x1="0" y1="0" x2="1" y2="1">
          <stop offset="0" stop-color="#9a9a9a"/>
          <stop offset="0.6" stop-color="#c4c4c4"/>
          <stop offset="1" stop-color="#e6e6e6"/>
        </linearGradient>
        <linearGradient id="rocker-fade" x1="0" y1="0" x2="1" y2="0">
          <stop offset="0" stop-color="#c8c8c8"/>
          <stop offset="1" stop-color="#e2e2e2"/>
        </linearGradient>
      </defs>
      <g class="rear-halftone" role="img" aria-label="Gray halftone dot field fading across the rear quarter">
        <polygon points="24,120 150,120 290,260 290,340 24,340" fill="url(#halftone-fade)"/>
      </g>
      <g class="accent-stripe">
        <polygon points="70,0 88,0 300,216 628,218 628,226 292,226" fill="var(--ink)"/>
      </g>
      <g class="rocker-band" role="img" aria-label="Gray halftone dot band along the lower body">
        <rect x="300" y="360" width="530" height="24" fill="url(#rocker-fade)"/>
      </g>
    </svg>

    <h1 class="brand-name">
      <span class="line-one">BROADVIEW</span>
      <span class="line-two">HOMES</span>
    </h1>
    <p class="tagline">RESIDENTIAL REMODELING</p>
    <p class="contact">
      <span class="phone">(555) - 214 -0386</span>
      <span class="web">BROADVIEWHOMESCT.COM</span>
      <span class="town">NORTH CALDER, CT</span>
    </p>
    <p class="license">LICENSE #HIC.0518274</p>
  </section>
</main>
</body>
</html>
```